Email flow for classic watch brand

We need to update our welcome flow with 3 emails. We want the design to reflect the brand and website www.kovanta.com. Our watches are unisex and the design needs to be light and modern.
The design will be the same for all but the message is different.
Email 1: Welcome
Email 2: Products
Email 3: Offer
I have attached PDFs of the emails we currently use and good examples on emails I like.
Emails need to be responsive and look great on all desktop and mobile.
Please use these lookbook images for the emails
https://files.plenmox.com/open?id=7QxRTzzn52KpfLmNDWqaVcXsTt
Kind regards
Fredrik Tolvmark
Logo and product images can be found here: https://files.plenmox.com/open?id=4H713yR8MUPLgk28jN9cWrHuKp
Target Market(s)
24-35 year olds with a fashion interest.
Industry/Entity Type
Fashion
Font styles to use
Look and feel
Each slider illustrates characteristics of the customer's brand and the style your logo design should communicate.

```html
<!DOCTYPE html>
<html lang="en">
<head>
<meta charset="utf-8">
<title>Kovanta – Thank You</title>
<link rel="stylesheet" href="https://fonts.googleapis.com/css2?family=EB+Garamond:ital,wght@0,400;0,500;0,700;1,400&display=swap">
<style>
  :root {
    --ink: #1b1b1b;
    --paper: #ffffff;
    --knit-light: #8d9093;
    --knit-mid: #5c6064;
    --knit-deep: #34373b;
    --skin: #8a6650;
    --dial: #e9e6e0;
    --leather-light: #a98462;
    --leather-mid: #7c5a3e;
    --leather-deep: #4c3424;
    --denim: #262a36;
  }
  * { margin: 0; padding: 0; box-sizing: border-box; }
  html, body { width: 1200px; height: 4520px; overflow: hidden; background: var(--paper); }
  body {
    font-family: "EB Garamond", "Times New Roman", serif;
    color: var(--ink);
    position: relative;
  }
  .email { position: relative; width: 1200px; height: 4520px; }

  .header { position: absolute; top: 0; left: 0; width: 1200px; height: 612px; text-align: center; }
  .brand-mark {
    position: absolute; top: 132px; left: 50%; transform: translateX(-50%);
    width: 96px; height: 96px; border-radius: 50%; background: var(--ink);
  }
  .brand-name {
    position: absolute; top: 296px; width: 100%;
    font-size: 132px; font-weight: 400; letter-spacing: 2px; line-height: 1;
  }
  .nav {
    position: absolute; top: 478px; width: 100%;
    display: flex; justify-content: center; gap: 84px;
    font-size: 60px; line-height: 1;
  }
  .nav a { color: var(--ink); text-decoration: none; }

  .hero {
    position: absolute; top: 612px; left: 0; width: 1200px; height: 836px;
    background:
      radial-gradient(ellipse 180px 150px at 640px 470px, rgba(233,230,224,0.55), rgba(233,230,224,0) 100%),
      radial-gradient(ellipse 300px 220px at 440px 300px, rgba(138,102,80,0.75), rgba(138,102,80,0) 100%),
      radial-gradient(ellipse 360px 260px at 150px 90px, rgba(150,152,154,0.9), rgba(150,152,154,0) 100%),
      radial-gradient(ellipse 520px 420px at 900px 620px, rgba(120,124,128,0.9), rgba(120,124,128,0) 100%),
      linear-gradient(160deg, var(--knit-mid) 0%, var(--knit-deep) 60%, #2a2d31 100%);
  }

  .thanks { position: absolute; top: 1612px; width: 100%; text-align: center; }
  .thanks h1 { font-size: 136px; font-weight: 400; letter-spacing: 3px; line-height: 1; }
  .thanks p { margin-top: 52px; font-size: 58px; line-height: 88px; }

  .gallery {
    position: absolute; top: 2268px; left: 0; width: 1200px; height: 780px;
    display: flex; gap: 8px;
  }
  .gallery-leather {
    width: 572px; height: 100%;
    background:
      radial-gradient(ellipse 110px 110px at 270px 470px, rgba(233,230,224,0.75), rgba(233,230,224,0) 100%),
      radial-gradient(ellipse 260px 160px at 200px 560px, rgba(196,164,128,0.6), rgba(196,164,128,0) 100%),
      radial-gradient(ellipse 320px 280px at 430px 180px, rgba(169,132,98,0.9), rgba(169,132,98,0) 100%),
      linear-gradient(135deg, var(--leather-mid) 0%, var(--leather-deep) 100%);
  }
  .gallery-knit {
    flex: 1; height: 100%;
    background:
      radial-gradient(ellipse 90px 90px at 250px 330px, rgba(233,230,224,0.6), rgba(233,230,224,0) 100%),
      radial-gradient(ellipse 260px 140px at 170px 380px, rgba(138,102,80,0.6), rgba(138,102,80,0) 100%),
      radial-gradient(ellipse 380px 200px at 360px 740px, rgba(38,42,54,0.95), rgba(38,42,54,0) 100%),
      radial-gradient(ellipse 320px 380px at 400px 200px, rgba(160,160,160,0.85), rgba(160,160,160,0) 100%),
      linear-gradient(160deg, var(--knit-light) 0%, var(--knit-mid) 100%);
  }

  .offer { position: absolute; top: 3176px; width: 100%; text-align: center; }
  .offer-lead { font-size: 62px; line-height: 96px; }
  .offer-amount { font-size: 104px; font-weight: 500; line-height: 112px; }
  .offer-code-note { margin-top: 96px; font-size: 66px; line-height: 92px; }
  .offer-code { font-weight: 700; }
  .offer-validity { font-style: italic; }

  .signoff { position: absolute; top: 3926px; width: 100%; text-align: center; font-size: 62px; line-height: 88px; }

  .social {
    position: absolute; top: 4212px; left: 0; width: 100%;
    display: flex; justify-content: center; gap: 24px;
  }
  .social-item { width: 88px; height: 88px; border-radius: 6px; background: var(--ink); display: block; }

  .footer {
    position: absolute; top: 4380px; width: 100%; text-align: center;
    font-size: 34px; line-height: 48px;
  }
  .footer a { color: var(--ink); font-weight: 700; text-decoration: none; }
</style>
</head>
<body>
<main class="email">
  <header class="header">
    <span class="brand-mark" aria-hidden="true"></span>
    <div class="brand-name">KOVANTA</div>
    <nav class="nav">
      <a href="#">Watches</a>
      <a href="#">Marrow Tweed Straps</a>
    </nav>
  </header>

  <div class="hero" role="img" aria-label="Lookbook photo: wrist wearing a classic watch with a white dial and dark strap against a grey knit sweater"></div>

  <section class="thanks">
    <h1>THANK YOU</h1>
    <p>We would like to thank you for<br>your interest in Kovanta watches.<br>Without your support, we would<br>not be where we are today.</p>
  </section>

  <section class="gallery">
    <div class="gallery-leather" role="img" aria-label="Lookbook photo: watch with white dial on a wrist beside a tan suede jacket"></div>
    <div class="gallery-knit" role="img" aria-label="Lookbook photo: hands and watch against a grey knit cardigan and dark trousers"></div>
  </section>

  <section class="offer">
    <p class="offer-lead">We would like to offer you</p>
    <p class="offer-amount">15% off</p>
    <p class="offer-lead">on your first purchase.</p>
    <p class="offer-code-note">Use the code <span class="offer-code">33FI-XHV3</span> (<span class="offer-validity">valid for<br>72h</span>) at the check out to receive the<br>discount.</p>
  </section>

  <section class="signoff">
    <p>King Regards,</p>
    <p>The Kovanta Team</p>
  </section>

  <nav class="social" aria-label="Social links">
    <a class="social-item" href="#" aria-label="Social profile 1"></a>
    <a class="social-item" href="#" aria-label="Social profile 2"></a>
    <a class="social-item" href="#" aria-label="Social profile 3"></a>
    <a class="social-item" href="#" aria-label="Social profile 4"></a>
  </nav>

  <footer class="footer">
    <p>No longer want to receive these emails? You can <a href="#">unsubscribe here.</a></p>
    <p>Kovanta Ltd.</p>
  </footer>
</main>
</body>
</html>
```